New Website for novelty yarn producer

We need a new website for our company, Tarvek. We make highly tailored yarns for weavers worldwide. This year marks our 40th anniversary and we want to evolve our image and identity.

Our temporary website can be found at:
www.tarvekyarns.com

Our only concern in that throughout the website the protagonist must be our client, we make their creations possible and are highly adaptable both during the ideation process of the yarn as well as in the production. This is at the core of the way we do business and is summarised within the concept of FPM (Fluid Partner Method).

Industry/Entity Type

Textile

Number of Pages Required

1 page

Colors
9bcb3c

Requirements
Must have
• Fluid Partner Method (FPM) - can be found on or current website www.tarvekyarns.com

```html
<!DOCTYPE html>
<html lang="en">
<head>
<meta charset="utf-8">
<title>Tarvek – Tailored weaving solutions</title>
<link href="https://fonts.googleapis.com/css2?family=Open+Sans:wght@400;600;700&family=Work+Sans:wght@300;400&display=swap" rel="stylesheet">
<style>
:root{
  --green:#9bcb3c;
  --green-dark:#86b52c;
  --ink:#1f1f1f;
  --text:#555;
  --muted:#777;
  --mist:#c7dcd6;
  --mist-dark:#b4cdc6;
  --panel:#f2f2f2;
  --footer:#1e1e1e;
  --white:#fff;
}
*{box-sizing:border-box;margin:0;padding:0}
html,body{width:1200px;height:2630px;overflow:hidden}
body{font-family:"Open Sans",Arial,sans-serif;color:var(--text);background:var(--white);position:relative}
.top-strip{height:4px;background:linear-gradient(90deg,var(--green) 0 35%,#8ed0c0 35% 60%,#7cc4e8 60% 80%,#f6e27a 80% 100%)}
.site-header{height:112px;display:flex;align-items:center;justify-content:space-between;padding:0 155px 0 160px}
.brand{font-family:"Work Sans",Arial,sans-serif;font-size:40px;color:var(--ink);letter-spacing:1px;font-weight:400}
.main-nav{display:flex;gap:19px;font-size:13px;font-weight:700;color:var(--ink)}
.main-nav .active{color:var(--green)}
.hero{height:540px;position:relative;text-align:center;background:linear-gradient(180deg,#cbdfd9 0%,#bfd7d0 60%,#b2c9c3 100%);overflow:hidden}
.hero-photo{position:absolute;inset:0;background:linear-gradient(180deg,rgba(0,0,0,0) 60%,rgba(180,140,160,.35) 85%,rgba(120,140,150,.35) 100%)}
.hero-title{position:relative;padding-top:76px;font-family:"Work Sans",Arial,sans-serif;font-weight:400;font-size:38px;color:var(--ink)}
.anniversary-badge{position:relative;width:300px;height:270px;margin:30px auto 0;border-radius:50%;background:radial-gradient(circle,rgba(155,203,60,.55) 0%,rgba(155,203,60,.25) 55%,rgba(155,203,60,0) 72%)}
.values{height:444px;display:flex;justify-content:center;gap:0;padding-top:66px;position:relative}
.values-line{position:absolute;top:140px;left:300px;width:600px;border-top:1px dotted #bbb}
.value{width:300px;text-align:center;position:relative}
.value-photo{width:152px;height:152px;border-radius:50%;margin:0 auto;border:3px dotted #9fc9bd;box-shadow:inset 0 0 0 4px var(--white)}
.value-photo.experience{background:linear-gradient(135deg,#3a3f4a,#8a2b2b 60%,#c9c6c0)}
.value-photo.creativity{background:linear-gradient(135deg,#f0c23a,#e8336f 50%,#1aa7b0)}
.value-photo.professionalism{background:linear-gradient(135deg,#1c2d4d,#d08a2a 55%,#1a2440)}
.value h3{font-size:14px;font-weight:700;color:var(--text);margin:16px 0 12px}
.value p{font-size:12.5px;line-height:20px;color:var(--muted);padding:0 12px}
.clients{height:305px;display:flex}
.clients-intro{width:536px;background:var(--green);color:var(--white);padding:50px 40px 0 160px}
.clients-intro h2{font-family:"Work Sans",Arial,sans-serif;font-weight:400;font-size:30px;margin-bottom:10px}
.clients-intro p{font-size:12.5px;line-height:19px;margin-bottom:30px}
.client-picker{display:flex;align-items:center;gap:8px;margin-left:-6px}
.client-picker .arrow{width:14px;height:20px}
.client-thumb{width:64px;height:64px;border-radius:50%;border:2px solid var(--white);background:linear-gradient(160deg,#a9a9a9,#6d6d6d)}
.client-thumb.tinted{background:linear-gradient(160deg,#c5d99a,#8aa85a)}
.client-portrait{width:203px;background:linear-gradient(180deg,#c9cccf 0%,#9a8c84 45%,#1c1c1c 75%,#111 100%)}
.client-quote{flex:1;background:var(--ink);color:var(--white);padding:52px 80px 0 34px;font-size:12.5px;line-height:19.5px}
.client-quote p+p{margin-top:19px}
.client-quote .name{color:var(--green);margin-top:19px;font-size:12px}
.numbers{height:275px;background:var(--panel);display:flex;padding:62px 0 0 160px}
.numbers-intro{width:300px;padding-top:24px}
.numbers-intro h2{font-family:"Work Sans",Arial,sans-serif;font-weight:400;font-size:30px;color:var(--ink);line-height:32px}
.numbers-intro .year{font-size:13px;color:var(--ink);display:block;margin-bottom:24px}
.btn{display:inline-block;font-size:12.5px;font-weight:700;color:var(--white);text-transform:uppercase;text-align:center;line-height:44px}
.btn-green{background:var(--green)}
.btn-dark{background:var(--ink)}
.stat{width:218px;text-align:center}
.stat svg{height:60px;display:block;margin:0 auto}
.stat .rule{width:56px;height:3px;background:var(--green);margin:8px auto 14px}
.stat .value-num{font-family:"Work Sans",Arial,sans-serif;font-size:38px;color:#444;line-height:42px}
.stat .label{font-size:12.5px;font-weight:600;color:#333;text-transform:uppercase;margin-top:8px}
.method{height:372px;background:linear-gradient(180deg,var(--mist) 0%,var(--mist-dark) 100%);text-align:center;padding-top:44px;color:var(--white)}
.method-mark{display:flex;justify-content:center;align-items:center;gap:18px}
.method-mark .mark-name{border-left:1px solid var(--white);padding-left:18px;text-align:left;font-family:"Work Sans",Arial,sans-serif;font-weight:300;font-size:17px;line-height:20px;text-transform:uppercase}
.method h2{font-family:"Work Sans",Arial,sans-serif;font-weight:400;font-size:30px;margin-top:28px}
.method p{font-size:12.5px;line-height:19px;width:560px;margin:8px auto 22px}
.heritage{height:220px;text-align:center;padding-top:44px}
.heritage p{width:540px;margin:0 auto 24px;font-size:14px;line-height:23px;color:var(--muted)}
.site-footer{height:358px;background:var(--footer);text-align:center;color:#ddd;font-size:11.5px;line-height:24px;padding-top:52px;position:relative}
.site-footer .brand{color:var(--white);font-size:34px;display:block;margin-bottom:24px}
.site-footer .copyright{position:absolute;left:0;right:0;bottom:26px;border-top:1px solid #333;padding-top:18px;color:var(--green);font-size:10.5px}
</style>
</head>
<body>
<div class="top-strip"></div>
<header class="site-header">
  <div class="brand">Tarvek</div>
  <nav class="main-nav">
    <span class="active">HOME</span><span>ABOUT US</span><span>FPM</span><span>HERITAGE</span><span>TEAM</span><span>BLOG</span><span>CONTACT</span>
  </nav>
</header>

<section class="hero">
  <div class="hero-photo" role="img" aria-label="Soft-focus photo of coloured thread spools on a table"></div>
  <h1 class="hero-title">Tailored weaving solutions</h1>
  <div class="anniversary-badge" role="img" aria-label="Celebrating 40th anniversary laurel emblem"></div>
</section>

<section class="values">
  <div class="values-line"></div>
  <article class="value">
    <div class="value-photo experience" role="img" aria-label="Photo of hands working at a loom"></div>
    <h3>Experience</h3>
    <p>Over the years the company has gained the knowledge and skills that define the superiority of our product and the rigor of our work ethic</p>
  </article>
  <article class="value">
    <div class="value-photo creativity" role="img" aria-label="Photo of colourful balls of yarn"></div>
    <h3>Creativity</h3>
    <p>Our belief is that the key to our clients' success is a combination of innovation, creativity and quality.<br>We strive to adapt and re-imagine our product, implementing these principles in order to meet and exceed our clients' demands (every time)</p>
  </article>
  <article class="value">
    <div class="value-photo professionalism" role="img" aria-label="Photo of yarn spools"></div>
    <h3>Professionality</h3>
    <p>We are a family business at the core. Our company is run with the same values as the Varesi family: respect, determination and</p>
  </article>
</section>

<section class="clients">
  <div class="clients-intro">
    <h2>Our Client</h2>
    <p>Our clients can expect open lines of communication, clarity and professionality. Our focus is our client.The success of a client is our success.</p>
    <div class="client-picker">
      <svg class="arrow" viewBox="0 0 14 20"><path d="M10 2 2 10l8 8" fill="none" stroke="#fff" stroke-width="1.5"/></svg>
      <div class="client-thumb" role="img" aria-label="Client portrait thumbnail"></div>
      <div class="client-thumb tinted" role="img" aria-label="Client portrait thumbnail"></div>
      <div class="client-thumb tinted" role="img" aria-label="Client portrait thumbnail"></div>
      <div class="client-thumb tinted" role="img" aria-label="Client portrait thumbnail"></div>
      <svg class="arrow" viewBox="0 0 14 20"><path d="M4 2l8 8-8 8" fill="none" stroke="#fff" stroke-width="1.5"/></svg>
    </div>
  </div>
  <div class="client-portrait" role="img" aria-label="Portrait photo of the featured client"></div>
  <blockquote class="client-quote">
    <p>Lorem ipsum dolor sit amet, consectetur adipiscing elit. Itaque hic ipse iam pridem est relectus; Quia, si mala sunt, is, qui erit in iis, beatus non erit. An me, inquam, nisi te audire vellem, censes haec dicturum fuisse? Nemo igitur esse beatus potest.</p>
    <p>Vide igitur ne non debeas verbis nostris uti, sententiis tuis.</p>
    <p class="name">-MAREN HOLT</p>
  </blockquote>
</section>

<section class="numbers">
  <div class="numbers-intro">
    <h2>TYS in Numbers</h2>
    <span class="year">2017</span>
    <span class="btn btn-green" style="width:150px">Find out more</span>
  </div>
  <div class="stat">
    <svg viewBox="0 0 60 60"><circle cx="30" cy="30" r="28" fill="none" stroke="#333" stroke-width="1.5" stroke-dasharray="2 3"/><text x="30" y="37" text-anchor="middle" font-family="Work Sans, sans-serif" font-size="19" fill="#333">40</text></svg>
    <div class="rule"></div>
    <div class="value-num">40</div>
    <div class="label">Years in business</div>
  </div>
  <div class="stat">
    <svg viewBox="0 0 60 60"><rect x="12" y="8" width="36" height="6" fill="none" stroke="#333" stroke-width="1.8"/><path d="M10 52 14 18h32l4 34z" fill="none" stroke="#333" stroke-width="1.8"/><circle cx="30" cy="35" r="10" fill="none" stroke="#333" stroke-width="1.8"/><path d="M30 35l4-6" stroke="#333" stroke-width="1.8"/></svg>
    <div class="rule"></div>
    <div class="value-num">2</div>
    <div class="label">Million kilograms/ yr</div>
  </div>
  <div class="stat">
    <svg viewBox="0 0 60 60"><path d="M16 10h16l18 18-18 18-18-18V12z" fill="none" stroke="#333" stroke-width="1.8" transform="rotate(10 30 30)"/><circle cx="22" cy="19" r="3" fill="none" stroke="#333" stroke-width="1.8"/></svg>
    <div class="rule"></div>
    <div class="value-num">8</div>
    <div class="label">Brands</div>
  </div>
</section>

<section class="method">
  <div class="method-mark">
    <svg width="60" height="60" viewBox="0 0 60 60"><circle cx="30" cy="30" r="26" fill="none" stroke="#fff" stroke-width="2"/></svg>
    <div class="mark-name">Fluid<br>Partner<br>Method</div>
  </div>
  <h2>Production built around you</h2>
  <p>Versatility and flexibility both in development and production are key in delivering a custom solution capable of giving life to your products.</p>
  <span class="btn btn-dark" style="width:150px">Find out more</span>
</section>

<section class="heritage">
  <p>Our team has decades of experience in providing yarn solutions to weavers around the world, assisting them in the creation of outstanding textiles.</p>
  <span class="btn btn-green" style="width:150px">Our heritage</span>
</section>

<footer class="site-footer">
  <span class="brand">Tarvek</span>
  <div>Corvane s.r.l</div>
  <div>Via dei Tessitori 14 - 59100 Prato - Italy - Tel. 0574 20418 r.a. - Fax 0574 208870</div>
  <div>R.E.A PO 418203 - Reg. Imp. PO 04127730481</div>
  <div>P. IVA 00427610972 - Cod. Fisc. 04127730481</div>
  <div>Capitale sociale € 91. 541, 99 int. ver.</div>
  <div class="copyright">© 2018 Tarvek. All Rights Reserved.</div>
</footer>
</body>
</html>
```